Trondel Group letterhead

Hi,

I need a letterhead template created for our business. This should be done in word format and A4 size. The images need to not move in the template ie when I am adding writing in etc. and should flow on when I get to a second page.

I have attached our logo templates below.

Other details to include on the letterhead somewhere are:

0438 571 962
Max@Trondelelectrical.example.com.au
PO Box 781 Marrowdale NSW 2163
ABN: 57 318 492 076

Thanks!

```html
<!DOCTYPE html>
<html lang="en">
<head>
<meta charset="utf-8">
<title>Trondel Group Letterhead</title>
<link href="https://fonts.googleapis.com/css2?family=Montserrat:wght@600;700&family=Open+Sans:wght@400;600&display=swap" rel="stylesheet">
<style>
  :root {
    --backdrop: #cfd4d4;
    --paper: #ffffff;
    --ink: #222222;
    --ink-soft: #3a3a3a;
    --accent: #ee5a24;
    --watermark-tone: #f4f4f4;
    --signature-tone: #f7c9b5;
  }
  * { margin: 0; padding: 0; box-sizing: border-box; }
  html, body {
    width: 1200px; height: 686px; overflow: hidden;
    background: var(--backdrop);
  }
  .canvas {
    position: relative; width: 1200px; height: 686px;
    display: flex; align-items: center; justify-content: center;
  }
  .letterhead {
    position: relative; width: 470px; height: 664px;
    background: var(--paper);
    font-family: "Open Sans", Arial, sans-serif;
    color: var(--ink);
    overflow: hidden;
  }
  .watermark-area {
    position: absolute; left: 150px; top: 150px; width: 290px; height: 290px;
    background: linear-gradient(135deg, var(--watermark-tone), #fbfbfb);
    border-radius: 8px;
  }
  .brand {
    position: absolute; left: 38px; top: 36px;
    display: flex; align-items: center; gap: 8px;
  }
  .brand-dot {
    width: 26px; height: 26px; border-radius: 50%;
    border: 3px solid var(--ink);
  }
  .brand-name {
    font-family: "Montserrat", Arial, sans-serif;
    font-weight: 700; font-size: 15px; letter-spacing: 0.5px;
    color: var(--accent); text-transform: uppercase;
  }
  .recipient {
    position: absolute; left: 38px; top: 160px; font-size: 9px; line-height: 1.4;
  }
  .recipient-date { margin-bottom: 6px; }
  .name-accent {
    font-family: "Montserrat", Arial, sans-serif;
    font-weight: 700; color: var(--accent);
  }
  .recipient-name { font-size: 12px; line-height: 1.2; }
  .recipient-role { margin-bottom: 6px; }
  .salutation {
    position: absolute; left: 38px; top: 248px; font-size: 13px;
  }
  .body-copy {
    position: absolute; left: 38px; top: 276px; width: 390px;
    font-size: 8.6px; line-height: 1.45; color: var(--ink-soft);
  }
  .body-copy p { margin-bottom: 11px; }
  .sign-off {
    position: absolute; left: 120px; top: 482px;
  }
  .signature-mark {
    width: 120px; height: 34px; border-radius: 6px;
    background: linear-gradient(90deg, var(--signature-tone), #fde6dc);
    margin-bottom: 4px;
  }
  .signer-name { font-size: 18px; line-height: 1.1; }
  .signer-role { font-size: 9px; }
  .contact-bar {
    position: absolute; left: 38px; right: 30px; bottom: 30px;
    display: flex; justify-content: space-between; align-items: flex-end;
    font-size: 8.4px; color: var(--ink); white-space: nowrap;
  }
  .contact-item { display: flex; align-items: center; gap: 4px; }
  .contact-stack { display: flex; flex-direction: column; gap: 6px; }
  .contact-accent { color: var(--accent); }
  .contact-plain { color: var(--ink); }
  .contact-icon { width: 9px; height: 9px; flex: none; }
</style>
</head>
<body>
<main class="canvas">
  <article class="letterhead">
    <div class="watermark-area" role="img" aria-label="Faint brand watermark area"></div>

    <header class="brand">
      <span class="brand-dot"></span>
      <span class="brand-name">Trondel Group</span>
    </header>

    <section class="recipient">
      <p class="recipient-date">August-05-2019</p>
      <p class="recipient-name name-accent">Renata Holloway</p>
      <p class="recipient-role">Director</p>
      <p>1840 Ridgeway Ave. Suite 310<br>Halbrook, TX 75480</p>
    </section>

    <p class="salutation name-accent">Renata Holloway</p>

    <section class="body-copy">
      <p>Lorem ipsum dolor sit amet, consectetuer adipiscing elit, sed diam nonummy nibh euismod tincidunt ut laoreet dolore magna aliquam erat volutpat. Ut wisi enim ad minim veniam, quis nostrud exerci tation ullamcorper suscipit lobortis</p>
      <p>Lorem ipsum dolor sit amet, cons ectetuer adipiscing elit, sed diam nonummy nibh euismod tincidunt ut laoreet dolore magna aliquam erat volutpat. Ut wisi enim ad minim veniam, quis nostrud exerci tation ullamcorper suscipit lobortis nisl ut aliquip ex ea commodo consequat. Lorem ipsum dolor sit amet, consectetuer olutpat. Ut wisi enim ad minim veniam, quis nostrud exerci tation ullamcorper suscipit lobortis nisl ut aliquip ex ea commodo consequat. Duis autem</p>
      <p>vel eum iriure dolor in hendrerit in vulputate velit esse molestie consequat, vel illum dolore eu feugiat nulla facilisis at vero eros et accumsan et iusto odio dignissim qui blandit praesent luptatum zzril delenit augue duis dolore te feugait nulla facilisi. Lorem ipsum dolor sit amet, cons ectetuer adipiscing elit, sed diam nonummy nibh euismod tincidunt ut laoreet dolore magna aliquam erat volutpat. Ut wisi enim .</p>
    </section>

    <section class="sign-off">
      <div class="signature-mark" role="img" aria-label="Handwritten signature"></div>
      <p class="signer-name name-accent">Owen Tarrant</p>
      <p class="signer-role">Co-Founder</p>
    </section>

    <footer class="contact-bar">
      <p class="contact-item">
        <svg class="contact-icon" viewBox="0 0 10 10" aria-hidden="true"><path d="M2 1l2 2-1 1.2c.6 1.2 1.5 2.1 2.8 2.8L7 6l2 2-1.4 1.4C4.5 9 1 5.5.6 2.4z" fill="var(--accent)"/></svg>
        0438 571 962
      </p>
      <div class="contact-stack">
        <p class="contact-accent">ABN: <span class="contact-plain">57 318 492 076</span></p>
        <p class="contact-item">
          <svg class="contact-icon" viewBox="0 0 10 10" aria-hidden="true"><rect x="0.5" y="2" width="9" height="6.5" rx="1" fill="var(--accent)"/><path d="M1 2.6l4 3 4-3" fill="none" stroke="#fff" stroke-width="0.9"/></svg>
          <span>Max@<span class="contact-accent">Trondelelectrical.example.com.au</span></span>
        </p>
      </div>
      <p class="contact-item">
        <svg class="contact-icon" viewBox="0 0 10 10" aria-hidden="true"><path d="M5 0.5a3.4 3.4 0 0 1 3.4 3.4C8.4 6.5 5 9.5 5 9.5S1.6 6.5 1.6 3.9A3.4 3.4 0 0 1 5 .5z" fill="var(--accent)"/><circle cx="5" cy="3.9" r="1.2" fill="#fff"/></svg>
        PO Box 781 Marrowdale NSW 2163
      </p>
    </footer>
  </article>
</main>
</body>
</html>
```